Etiketten-Design für familiengeführten Weinbaubetrieb
Zielgruppe
Wir sind ein Familiengeführter Weinbaubetrieb und vermarkten unseren Wein in 0,75l Flaschen sowie auch Säfte und Schnäpse.
Zur zeit Verkaufen wir unseren Wein an Gastro und Private Kunden auch teils über Messen
Aufgabenstellung
Das derzeitige Etikett ist recht schlicht gestaltet und das Logo besteht rein aus dem geschriebenen Namen Winzerhof Dolmeck. Es kann aber auch gerne nur mit dem Namen Dolmeck ohne Winzerhof gearbeitet werden! Mit dem einbringen einer neuen Generation in den Betrieb wollen wir das aussehen unserer Produkte erneuern. Dazu kann sich gerne mit dem Namen als 'Logo' in jeglicher Art gespielt werden. Wir füllen unsere Weine in 0,75l Bordeaux Flaschen. Die Form des Etikett ist kein K.O. Kriterium jedoch wurde ursprünglich ein rund um Etikett angedacht. Sollten die Designes sich auch anders realisieren lassen sind wir gerne offen für Ideen.

```html
<!DOCTYPE html>
<html lang="de">
<head>
<meta charset="utf-8">
<title>Etikett – Winzerhof Dolmeck, Grüner Veltliner 2023</title>
<link href="https://fonts.googleapis.com/css2?family=EB+Garamond:wght@400;500&display=swap" rel="stylesheet">
<style>
  :root {
    --page: #ffffff;
    --paper: #f2f2f1;
    --paper-edge: #e4e4e2;
    --gold: #d9a21b;
    --ink: #1a1a1a;
  }
  html, body {
    margin: 0;
    padding: 0;
    width: 1200px;
    height: 1200px;
    overflow: hidden;
    background: var(--page);
  }
  .canvas {
    position: relative;
    width: 1200px;
    height: 1200px;
    font-family: "EB Garamond", Georgia, serif;
  }
  .label {
    position: absolute;
    left: 286px;
    top: 118px;
    width: 628px;
    height: 964px;
    background: linear-gradient(180deg, #f5f5f4 0%, var(--paper) 55%, #efefed 100%);
    box-shadow: 0 0 0 1px var(--paper-edge);
    text-align: center;
  }
  .brand {
    position: absolute;
    left: 50%;
    top: 270px;
    transform: translate(-50%, -50%);
    width: 300px;
    height: 300px;
    border: 3px solid var(--gold);
    border-radius: 50%;
    display: flex;
    align-items: center;
    justify-content: center;
    box-sizing: border-box;
  }
  .brand-name {
    color: var(--gold);
    font-weight: 500;
    font-size: 40px;
    line-height: 1.1;
    letter-spacing: 0.04em;
    margin: 0;
  }
  .wine {
    position: absolute;
    left: 0;
    right: 0;
    top: 600px;
    color: var(--ink);
    font-weight: 400;
    font-size: 44px;
    line-height: 1.4;
    margin: 0;
  }
  .producer {
    position: absolute;
    left: 0;
    right: 0;
    top: 778px;
    color: var(--gold);
    font-size: 21px;
    line-height: 1.35;
    margin: 0;
  }
  .facts {
    position: absolute;
    left: 130px;
    right: 130px;
    top: 895px;
    display: flex;
    justify-content: space-between;
    color: var(--ink);
    font-size: 19px;
    margin: 0;
  }
</style>
</head>
<body>
  <main class="canvas">
    <section class="label" aria-label="Flaschenetikett">
      <div class="brand">
        <p class="brand-name">Winzerhof<br>Dolmeck</p>
      </div>
      <h1 class="wine">Grüner Veltliner<br>2023</h1>
      <p class="producer">Erzeugerabfüllung<br>Winzerhof Dolmeck<br>A-2231 Niederau 12</p>
      <p class="facts"><span>0,7% L</span><span>trocken</span><span>Alc. 13% vol</span></p>
    </section>
  </main>
</body>
</html>
```